TALVORIK

The business want a professional looking business card. We have a scetch we will add but want the extra upgrade, and would like more suggestions for variations of our business cards.

```html
<!DOCTYPE html>
<html lang="en">
<head>
<meta charset="utf-8">
<title>Talvorik Business Cards</title>
<link rel="stylesheet" href="https://fonts.googleapis.com/css2?family=Jost:wght@300;400;500&display=swap">
<style>
  :root {
    --backdrop: #3d3d3d;
    --paper: #ffffff;
    --gold-deep: #6e4f27;
    --gold-mid: #9c7a40;
    --gold-light: #c29852;
    --gold-glow: #d6ac62;
    --gold-text: #a57f3e;
    --ink-light: #ffffff;
  }
  * { margin: 0; padding: 0; box-sizing: border-box; }
  html, body {
    width: 1200px; height: 1200px; overflow: hidden;
    background: var(--backdrop);
    font-family: "Jost", "Futura", sans-serif;
  }
  .canvas { position: relative; width: 1200px; height: 1200px; }

  .card {
    position: absolute;
    width: 689px; height: 394px;
    border-radius: 28px;
    overflow: hidden;
    box-shadow: 0 6px 18px rgba(0,0,0,0.35);
  }
  .card--front { left: 266px; top: 158px; background: var(--paper); }
  .card--back {
    left: 263px; top: 653px;
    background: radial-gradient(ellipse 60% 70% at 50% 42%, var(--gold-glow) 0%, #b88f4c 45%, var(--gold-deep) 100%);
  }

  .front-sweep { position: absolute; inset: 0; width: 100%; height: 100%; }

  .brand {
    position: absolute; left: 56px; top: 178px; width: 210px;
    text-align: center; color: var(--gold-text);
  }
  .brand__name {
    font-weight: 500; font-size: 30px; letter-spacing: 7px;
    line-height: 1; padding-left: 7px;
  }
  .brand__since {
    margin-top: 10px; font-size: 9px; letter-spacing: 5px; font-weight: 400;
    padding-left: 5px;
  }

  .person {
    position: absolute; right: 27px; top: 242px; text-align: right; color: var(--ink-light);
  }
  .person__name { font-size: 22px; font-weight: 400; line-height: 1; letter-spacing: -0.2px; }
  .person__role { font-size: 16px; font-weight: 300; margin-top: 6px; line-height: 1; }

  .contacts {
    position: absolute; right: 27px; top: 303px;
    list-style: none; color: var(--ink-light);
    font-weight: 300; font-size: 17px; line-height: 21px;
  }
  .contacts__item { display: flex; justify-content: flex-end; align-items: center; gap: 10px; }
  .contacts__icon { width: 12px; height: 12px; flex: none; }

  .back-name {
    position: absolute; left: 0; right: 0; top: 176px;
    text-align: center; color: var(--ink-light);
    font-size: 40px; font-weight: 400; letter-spacing: 10px; padding-left: 10px;
  }
  .back-url {
    position: absolute; left: 0; right: 0; top: 302px;
    text-align: center; color: var(--ink-light);
    font-size: 16px; font-weight: 300; letter-spacing: 4px;
  }
</style>
</head>
<body>
<main class="canvas">
  <section class="card card--front" aria-label="Business card front">
    <svg class="front-sweep" viewBox="0 0 689 394" preserveAspectRatio="none" aria-hidden="true">
      <defs>
        <linearGradient id="sweepGold" x1="0" y1="0" x2="1" y2="0">
          <stop offset="0" stop-color="#6e5028"/>
          <stop offset="0.55" stop-color="#a07c40"/>
          <stop offset="1" stop-color="#c09652"/>
        </linearGradient>
      </defs>
      <path d="M689,14 C560,140 420,250 300,288 C200,320 100,324 0,312 L0,394 L689,394 Z" fill="url(#sweepGold)"/>
      <path d="M0,290 C110,308 220,302 300,288 C200,318 100,324 0,312 Z" fill="#c29650"/>
      <path d="M0,312 C100,324 200,318 300,288" fill="none" stroke="#ffffff" stroke-width="1"/>
    </svg>

    <div class="brand">
      <div class="brand__name">TALVORIK</div>
      <div class="brand__since">SINCE 2026</div>
    </div>

    <div class="person">
      <div class="person__name">Lars Henrik Solvang</div>
      <div class="person__role">CEO &amp; Founder</div>
    </div>

    <ul class="contacts">
      <li class="contacts__item">004790015526
        <svg class="contacts__icon" viewBox="0 0 12 12" aria-hidden="true"><rect x="3" y="0.8" width="6.4" height="10.4" rx="1" fill="none" stroke="#fff" stroke-width="1.4"/></svg>
      </li>
      <li class="contacts__item">talvorik.llc@postmail.com
        <svg class="contacts__icon" viewBox="0 0 12 12" aria-hidden="true"><rect x="0.5" y="2.5" width="11" height="7" fill="#fff"/><path d="M0.5,2.8 L6,6.6 L11.5,2.8" fill="none" stroke="#a8844a" stroke-width="1"/></svg>
      </li>
      <li class="contacts__item">www.talvorik.llc
        <svg class="contacts__icon" viewBox="0 0 12 12" aria-hidden="true"><circle cx="6" cy="6" r="5.5" fill="#fff"/><path d="M4,3 C6,4 5,6 3.5,7 M7.5,6 C9,7 8.5,9 7,10" fill="none" stroke="#b08a4c" stroke-width="1.3"/></svg>
      </li>
    </ul>
  </section>

  <section class="card card--back" aria-label="Business card back">
    <div class="back-name">TALVORIK</div>
    <div class="back-url">www.talvorik.llc</div>
  </section>
</main>
</body>
</html>
```